Vardena General Painting Ltd. - Construction painting company providing high-quality service

We need a logo and business card design for a painting company that provides high-quality work for major developers and builders in Calgary, Alberta. Our projects include commercial high-rise residential towers. We would like designs that communicate professionalism and high quality service.
Updates
Need extra days to review
Target Market(s)
Developers and builders
Industry/Entity Type
Construction
Contact Information for Business Card
Company name, employee name, title, phone number, email address
Font styles to use
Colors
Designer to choose colors to be used in the design.
Look and feel
Each slider illustrates characteristics of the customer's brand and the style your logo design should communicate.

```html
<!DOCTYPE html>
<html lang="en">
<head>
<meta charset="utf-8">
<title>Vardena General Painting Ltd. – Business Card</title>
<link rel="stylesheet" href="https://fonts.googleapis.com/css2?family=Poppins:wght@400;500;600;700&display=swap">
<style>
  :root {
    --stage: #3a3d42;
    --navy: #241f6b;
    --navy-soft: #2c2878;
    --sky: #33c1ef;
    --amber: #fbb417;
    --paper: #ffffff;
    --ink: #1f1b5e;
  }
  * { box-sizing: border-box; margin: 0; padding: 0; }
  html, body { width: 1200px; height: 1000px; overflow: hidden; }
  body {
    background: var(--stage);
    font-family: "Poppins", sans-serif;
    position: relative;
  }
  .card {
    position: absolute;
    left: 250px;
    width: 700px;
    height: 400px;
    border-radius: 22px;
    overflow: hidden;
  }
  .card--back { top: 60px; background: var(--navy); }
  .card--front { top: 540px; background: var(--paper); }

  .brand {
    position: absolute;
    display: flex;
    align-items: center;
    gap: 18px;
  }
  .brand__dot {
    width: 58px; height: 58px;
    border-radius: 50%;
    flex: none;
  }
  .brand__name {
    font-weight: 700;
    text-transform: uppercase;
    line-height: 1.05;
    letter-spacing: 0.5px;
  }
  .card--back .brand { left: 160px; top: 150px; }
  .card--back .brand__dot { background: var(--amber); }
  .card--back .brand__name { color: var(--sky); font-size: 36px; }

  .card--front .brand { left: 40px; top: 110px; width: 290px; flex-direction: column; align-items: flex-start; gap: 14px; }
  .card--front .brand__dot { background: var(--sky); }
  .card--front .brand__name { color: var(--ink); font-size: 27px; }

  .divider {
    position: absolute;
    left: 345px; top: 70px;
    width: 2px; height: 190px;
    background: var(--sky);
  }
  .contact {
    position: absolute;
    left: 375px; top: 95px;
    color: var(--ink);
  }
  .contact__name { font-size: 24px; font-weight: 600; line-height: 1.2; }
  .contact__title { font-size: 18px; font-weight: 500; color: var(--sky); margin-bottom: 14px; }
  .contact__row { display: flex; align-items: center; gap: 10px; font-size: 15px; margin-top: 8px; }
  .contact__icon {
    width: 24px; height: 24px; border-radius: 50%;
    background: var(--amber);
    display: flex; align-items: center; justify-content: center;
    flex: none;
  }
  .splash {
    position: absolute;
    left: 0; bottom: 0;
    width: 700px; height: 130px;
  }
</style>
</head>
<body>
  <section class="card card--back" aria-label="Card back">
    <div class="brand">
      <span class="brand__dot"></span>
      <p class="brand__name">Vardena General<br>Painting Ltd.</p>
    </div>
  </section>

  <section class="card card--front" aria-label="Card front">
    <div class="brand">
      <span class="brand__dot"></span>
      <p class="brand__name">Vardena General<br>Painting Ltd.</p>
    </div>
    <div class="divider"></div>
    <div class="contact">
      <p class="contact__name">Marcus Ellery</p>
      <p class="contact__title">Principal</p>
      <p class="contact__row">
        <span class="contact__icon">
          <svg width="13" height="13" viewBox="0 0 24 24" fill="#fff"><path d="M6.6 10.8a15.1 15.1 0 0 0 6.6 6.6l2.2-2.2c.3-.3.7-.4 1-.2 1.1.4 2.3.6 3.6.6.6 0 1 .4 1 1V20c0 .6-.4 1-1 1A17 17 0 0 1 3 4c0-.6.4-1 1-1h3.5c.6 0 1 .4 1 1 0 1.3.2 2.5.6 3.6.1.3 0 .7-.2 1z"/></svg>
        </span>
        0481-5520-7714
      </p>
      <p class="contact__row">
        <span class="contact__icon">
          <svg width="13" height="13" viewBox="0 0 24 24" fill="none" stroke="#fff" stroke-width="2.4"><rect x="3" y="5" width="18" height="14" rx="1"/><path d="M3 6l9 7 9-7"/></svg>
        </span>
        info@vardenapainting.com
      </p>
    </div>
    <svg class="splash" viewBox="0 0 700 130" role="img" aria-label="Blue and yellow paint splash decoration along the bottom edge" preserveAspectRatio="none">
      <defs>
        <linearGradient id="splashTone" x1="0" y1="0" x2="1" y2="0">
          <stop offset="0" stop-color="#33c1ef"/>
          <stop offset="0.5" stop-color="#5fc7e0"/>
          <stop offset="1" stop-color="#fbb417"/>
        </linearGradient>
      </defs>
      <path d="M0 10 C150 40 300 50 420 85 C520 110 620 100 700 60 L700 130 L0 130 Z" fill="url(#splashTone)"/>
    </svg>
  </section>
</body>
</html>
```